Kerno Solutions: searching for a flyer to trow in letterboxes for properties we are interested in

Hello ,

Introduction:
We are a company based in Luxembourg called "Kerno Solutions". We are specialized in buying properties on which we develop and build constructions before selling them.

Informations for the flyer:
We need a flyer to trow into the letter boxes of property owners letting them know that we are interested in buying their property, if they are interested they can give us a call.

The text for the flyer/letter is in the attachment called >>2020-03-11_KS_Text for flyer,letter there might be slight changes<<.

We need to look competent, professional and financially stable.

The flyer needs to be short and not over welling with information otherwise it will land in the trash.

We have decided that we don't want real pictures on the flyer, but shapes of any kind, blue prints, drawings are fine.

Format should be in DIN A4. We plan to print the flyer on both sides in two different languages, in other words the design will be the same on both sides only the text will be in a different language.

I also added our current logo and here is the design of the website that is under construction at the moment http://www.kernosolutions-example.lu/. The logo's color can be changed into a different blue or uni color (all white or all black).
Updates

Hi, First time user the howl thing started faster as expected. Furthermore, I need to catch my boss to discust the project with him and he is on a lot of meetings. Please give us a little bit more time. Thanks

Target Market(s)

Property owners

Requirements
Must have
• email, phone number, tax number (RCS), Tax number , matriculation and address.
see word file in attachment for information
Nice to have
• Our company logo, in one form or an other, you can be creative, the logo is in the attachment.
Should not have
• Real pictures

```html
<!DOCTYPE html>
<html lang="fr">
<head>
<meta charset="utf-8">
<title>Kerno Solutions – Courrier</title>
<link href="https://fonts.googleapis.com/css2?family=Bebas+Neue&family=Inter:wght@400;500;700&display=swap" rel="stylesheet">
<style>
  :root {
    --brand-blue: #1c6bbd;
    --header-bg: #eef4f6;
    --ink: #111111;
    --footer-teal: #11606a;
    --frame-dark: #0f1d2b;
    --white: #ffffff;
  }
  * { box-sizing: border-box; margin: 0; padding: 0; }
  html, body { width: 857px; height: 1200px; overflow: hidden; background: var(--white); }
  .page {
    position: relative;
    width: 857px;
    height: 1200px;
    overflow: hidden;
    background: var(--white);
    font-family: "Inter", Arial, sans-serif;
    color: var(--ink);
  }
  .letterhead {
    position: absolute;
    left: 13px; right: 11px;
    top: 59px; height: 115px;
    background: var(--header-bg);
    text-align: center;
    padding-top: 30px;
  }
  .letterhead__name {
    font-family: "Bebas Neue", Impact, sans-serif;
    font-weight: 400;
    font-size: 42px;
    letter-spacing: 1px;
    color: var(--brand-blue);
    line-height: 1;
  }
  .letterhead__address {
    margin-top: 4px;
    font-size: 11px;
    color: var(--ink);
  }
  .letter-body {
    position: absolute;
    left: 106px;
    top: 278px;
    width: 625px;
    font-size: 17px;
    line-height: 21px;
  }
  .letter-body p { margin: 0; }
  .letter-body .greeting { margin-bottom: 46px; }
  .letter-body .intro { margin-bottom: 46px; }
  .letter-body .offer { margin-bottom: 13px; }
  .letter-body .availability { margin-bottom: 51px; }
  .letter-body .closing { margin-bottom: 62px; }
  .footer-band {
    position: absolute;
    left: 13px; right: 11px;
    top: 945px; bottom: 9px;
    background: var(--footer-teal);
  }
  .brand-plate {
    position: absolute;
    left: 300px; top: 855px;
    width: 263px; height: 189px;
    background: var(--white);
    border: 10px solid var(--frame-dark);
    box-shadow: 3px 4px 8px rgba(0,0,0,0.35);
    display: flex;
    align-items: center;
    justify-content: center;
    gap: 10px;
  }
  .brand-plate__mark {
    width: 22px; height: 22px;
    background: var(--brand-blue);
  }
  .brand-plate__name {
    font-family: "Inter", Arial, sans-serif;
    font-weight: 700;
    font-size: 20px;
    color: var(--brand-blue);
    white-space: nowrap;
  }
  .contact-row {
    position: absolute;
    top: 1100px;
    left: 13px; right: 11px;
    padding: 0 40px 0 50px;
    display: flex;
    justify-content: space-between;
    align-items: center;
    color: var(--white);
    font-size: 16px;
  }
  .contact-item {
    display: flex;
    align-items: center;
    gap: 9px;
    white-space: nowrap;
  }
  .contact-item svg { width: 21px; height: 21px; stroke: var(--white); fill: none; stroke-width: 1.5; flex: none; }
</style>
</head>
<body>
<div class="page">
  <header class="letterhead">
    <h1 class="letterhead__name">KERNO SOLUTIONS SÀRL</h1>
    <p class="letterhead__address">18 rue des Tilleuls, L-3390 Peppange</p>
  </header>

  <main class="letter-body">
    <p class="greeting">Madame, Monsieur,</p>
    <p class="intro">Ce courrier vous a été adressé, car votre propriété a attiré notre attention. Nous souhaiterions discuter avec vous de son éventuel rachat par notre société.</p>
    <p class="offer">En cas d’accord, nous vous assurons une décision rapide, un paiement garanti, et zéro frais d’intermédiaire.</p>
    <p class="availability">En attendant de vos nouvelles, nous restons à votre entière disposition pour tout renseignement.</p>
    <p class="closing">Salutations distinguées,</p>
    <p class="signature">L’équipe de Kerno Solutions</p>
  </main>

  <div class="footer-band"></div>

  <div class="brand-plate">
    <span class="brand-plate__mark"></span>
    <span class="brand-plate__name">KERNO SOLUTIONS</span>
  </div>

  <footer class="contact-row">
    <div class="contact-item contact-item--phone">
      <svg viewBox="0 0 24 24"><path d="M5 3h4l2 5-2.5 1.5a11 11 0 0 0 6 6L16 13l5 2v4a2 2 0 0 1-2 2A16 16 0 0 1 3 5a2 2 0 0 1 2-2z"/></svg>
      <span>691 000 000</span>
    </div>
    <div class="contact-item contact-item--mail">
      <svg viewBox="0 0 24 24"><path d="M22 2 11 13"/><path d="M22 2 15 22l-4-9-9-4z"/></svg>
      <span>info@kernosolutions-example.lu</span>
    </div>
    <div class="contact-item contact-item--web">
      <svg viewBox="0 0 24 24"><circle cx="12" cy="12" r="10"/><path d="M2 12h20"/><path d="M12 2a15 15 0 0 1 0 20a15 15 0 0 1 0-20z"/></svg>
      <span>www.kernosolutions-example.lu</span>
    </div>
  </footer>
</div>
</body>
</html>
```